Economic Forum- Save the Date

Two part project.

First-Need a save the date that will ultimately be a flyer/invite for our Economic Summit held in Dallas, TX.

The combined BRM/TLO Economic Forum will be held on January 14th, 2015 from 4-8pm at the Verlaine Hotel in the newly refinished Sovereign Ballroom.

Keynote Speakers: Marcus Feldweather, Economist and Research Director for the Ridgeton Monetary Bureau for over 4 decades.
Gordon Pellingham as the panel moderator, leading a 3 person panel discussion.
Ned Hollis, incoming Chairman of the Board of KPR Airport, and a long time aviation expert, to speak at the Professional Development Session.

Second-the save the date will turn into an invite with more detailed info added as well as timeline and sponsor logos. Need this available in pdf and jpeg in order to use digitally.
Updates

I added the second logo so please work that in...sorry!

Target Market(s)

Mid to Late career seasoned business professionals including CFO, CEO's, COO's, Principals, Pres and Vice Pres, Managing Directors, ages 30-60, attending a formal Economic event.

Industry/Entity Type

Hotel

Font styles to use
Other font styles liked:
• I'm open to fonts and prefer creative use of fonts/colors yet not too busy

Requirements
Must have
• Must have an initial save the date design with basic info that will be edited and ultimately used a digital invitation/flyer to draw people to event. Bold, modern appeal- geometrics may work well. Two logos will be used as hosts of event and need to be worked into design. Clear and easy to read fonts but creative
Nice to have
• ?
Should not have
• ?

```html
<!DOCTYPE html>
<html lang="en">
<head>
<meta charset="utf-8">
<title>Economic Forum – Save the Date</title>
<link rel="stylesheet" href="https://fonts.googleapis.com/css2?family=Nunito:ital,wght@0,300;0,400;0,600;0,700;0,800;1,400&display=swap">
<style>
  :root {
    --green: #7ed321;
    --orange: #f5a623;
    --blue: #1f7cc0;
    --ink: #3a3a3a;
    --grey: #8a8a8a;
    --white: #ffffff;
  }
  * { margin: 0; padding: 0; box-sizing: border-box; }
  html, body { width: 1200px; height: 1200px; overflow: hidden; background: var(--white); }
  .flyer {
    position: relative; width: 1200px; height: 1200px; overflow: hidden;
    font-family: "Nunito", Arial, sans-serif; color: var(--ink); background: var(--white);
  }
  .shapes { position: absolute; inset: 0; }
  .headline {
    position: absolute; top: 18px; left: 0; width: 100%; text-align: center;
    color: var(--white); font-weight: 800; font-size: 70px; letter-spacing: 5px;
  }
  .host { position: absolute; font-weight: 800; font-size: 92px; line-height: 1; }
  .host--left { left: 28px; top: 222px; color: var(--grey); }
  .host--right { left: 318px; top: 238px; color: var(--blue); font-size: 70px; }
  .host-divider { position: absolute; left: 282px; top: 210px; width: 3px; height: 125px; background: var(--green); }
  .event-title {
    position: absolute; left: 748px; top: 200px; color: var(--orange);
    font-weight: 400; font-size: 82px; line-height: 1.0;
  }
  .event-date {
    position: absolute; right: 36px; top: 398px; text-align: right; color: var(--white);
    font-weight: 400; font-size: 64px; line-height: 1.05;
  }
  .event-place {
    position: absolute; right: 36px; top: 540px; text-align: right; color: var(--white);
    font-size: 30px; line-height: 1.5;
  }
  .speaker-name { position: absolute; color: var(--blue); font-size: 33px; line-height: 1.15; font-weight: 400; }
  .speaker-name strong { display: block; font-weight: 800; }
  .speaker-name--one { left: 20px; top: 400px; }
  .speaker-name--two { left: 240px; top: 465px; }
  .speaker-name--three { left: 440px; top: 400px; width: 196px; text-align: right; }
  .speaker-bio { position: absolute; font-size: 20px; line-height: 1.3; color: var(--ink); }
  .speaker-bio--one { left: 20px; top: 745px; width: 188px; }
  .speaker-bio--two { left: 240px; top: 815px; width: 180px; }
  .speaker-bio--three { left: 440px; top: 775px; width: 210px; }
  .invite { position: absolute; left: 795px; top: 843px; color: var(--grey); font-size: 38px; }
  .phone { position: absolute; left: 722px; top: 892px; color: var(--orange); font-size: 62px; font-weight: 400; letter-spacing: 1px; }
  .target-label { position: absolute; left: 44px; top: 1012px; color: var(--blue); font-weight: 700; font-size: 27px; }
  .target-text {
    position: absolute; left: 44px; top: 1050px; width: 1110px; color: var(--grey);
    font-style: italic; font-size: 21px; line-height: 1.3;
  }
</style>
</head>
<body>
<main class="flyer">
  <svg class="shapes" width="1200" height="1200" viewBox="0 0 1200 1200">
    <polygon class="header-band" points="0,0 1200,0 1200,112 0,112" fill="var(--green)"/>
    <polygon class="header-accent" points="760,126 1200,112 1200,140 760,134" fill="var(--orange)"/>
    <polygon class="date-panel" points="690,372 1200,362 1200,742 746,672" fill="var(--green)"/>
    <defs>
      <linearGradient id="portrait" x1="0" y1="0" x2="0" y2="1">
        <stop offset="0" stop-color="#8d97a6"/>
        <stop offset="1" stop-color="#3b4250"/>
      </linearGradient>
    </defs>
    <polygon role="img" aria-label="Portrait photo of Marcus Feldweather" points="0,485 200,485 200,725 0,732" fill="url(#portrait)"/>
    <polygon role="img" aria-label="Portrait photo of Gordon Pellingham" points="218,560 422,560 422,795 218,788" fill="url(#portrait)"/>
    <polygon role="img" aria-label="Portrait photo of Ned Hollis" points="440,515 640,515 640,750 440,744" fill="url(#portrait)"/>
    <polygon class="target-marker" points="0,1000 30,1022 0,1044" fill="var(--green)"/>
    <polygon class="footer-accent" points="0,1128 1200,1118 1200,1126 0,1136" fill="var(--orange)"/>
    <polygon class="footer-band" points="0,1136 1200,1126 1200,1200 0,1200" fill="var(--green)"/>
  </svg>

  <h1 class="headline">SAVE THE DATE!</h1>

  <div class="host host--left">BRM</div>
  <div class="host-divider"></div>
  <div class="host host--right">TLO</div>

  <h2 class="event-title">Economic<br>Forum</h2>

  <p class="event-date">January 14th<br>2015</p>
  <p class="event-place">4-8pm at the Verlaine Hotel<br>Dallas, Texas</p>

  <p class="speaker-name speaker-name--one">Marcus<strong>Feldweather</strong></p>
  <p class="speaker-name speaker-name--two">Gordon<strong>Pellingham</strong></p>
  <p class="speaker-name speaker-name--three">Ned<strong>Hollis</strong></p>

  <p class="speaker-bio speaker-bio--one">Economist and Research Director for the Ridgeton Monetary Bureau for over 4 decades.</p>
  <p class="speaker-bio speaker-bio--two">As the panel moderator, leading a 3 person panel discussion.</p>
  <p class="speaker-bio speaker-bio--three">Incoming Chairman of the Board of KPR Airport, and a long time aviation expert, to speak at the Professional Development Session.</p>

  <p class="invite">Please join us!</p>
  <p class="phone">000-000-0000</p>

  <p class="target-label">Target</p>
  <p class="target-text">Mid to Late career seasoned business professionals including CFO, CEO's, COO's, Principals, Pres and Vice Pres, Managing Directors, ages 30-60, attending a formal Economic event.</p>
</main>
</body>
</html>
```